Maplerise Trading Inc. needs an innovative idea for letterhead and visiting cards.

Maplerise Trading Inc. is a Canadian brand since 2007. It is a renown dealer of kids and office furniture locally. Moreover, exporting electric fixtures e.g. switches, LED's, down-lights etc. to Middle East and Africa. We have initiated a number of steps including re-branding, to boost our export in 2020. We have successfully designed our new logo a few months ago through 'Artfolio' and now we are looking for an innovative idea for a letterhead.
Some key points:
• Red, black and white are the three colors used in all our packaging and furniture. (grey is optional)
• Shouldn’t be too wide.
• Use of watermark is preferable.
• You can visit our North American site at www.mapleriseinc.com. Export website of the company will be launched soon. www.mapleriseinc.ca
• Same letterhead will be used locally and internationally.
• Our new logo and sample packaging is attached.

```html
<!DOCTYPE html>
<html lang="en">
<head>
<meta charset="utf-8">
<title>Maplerise Trading Inc. — Letterhead</title>
<link rel="stylesheet" href="https://fonts.googleapis.com/css2?family=Lato:wght@400;700&family=Questrial&family=Pinyon+Script&display=swap">
<style>
  :root {
    --backdrop: #dedede;
    --paper: #efefef;
    --ink: #3b3b3b;
    --ink-soft: #555555;
    --brand-red: #8e0a10;
    --brand-black: #121212;
    --rule-white: #f7f7f7;
  }
  * { box-sizing: border-box; margin: 0; padding: 0; }
  html, body {
    width: 1200px;
    height: 1017px;
    overflow: hidden;
    background: var(--backdrop);
  }
  .letterhead {
    position: absolute;
    left: 232px;
    top: 30px;
    width: 736px;
    height: 957px;
    background: var(--paper);
    box-shadow: 0 6px 18px rgba(0,0,0,0.18);
    overflow: hidden;
    font-family: "Lato", Arial, sans-serif;
    color: var(--ink);
  }
  .header-wave {
    position: absolute;
    left: 0;
    top: 0;
    width: 736px;
    height: 153px;
    display: block;
  }
  .brand {
    position: absolute;
    left: 63px;
    top: 134px;
    display: flex;
    align-items: center;
    gap: 12px;
  }
  .brand-square {
    width: 58px;
    height: 58px;
    background: var(--brand-red);
    border-radius: 6px;
  }
  .brand-name {
    font-family: "Lato", Arial, sans-serif;
    font-weight: 400;
    font-size: 30px;
    line-height: 32px;
    color: var(--ink);
    letter-spacing: 0.5px;
  }
  .letter-body {
    position: absolute;
    left: 63px;
    top: 276px;
    width: 652px;
    font-size: 10.3px;
    line-height: 18.1px;
    color: var(--ink);
  }
  .letter-body p + p { margin-top: 18px; }
  .signer {
    position: absolute;
    left: 63px;
    top: 654px;
  }
  .signer-name {
    font-size: 13px;
    color: var(--brand-red);
    letter-spacing: 0.2px;
  }
  .signer-role {
    font-size: 6.5px;
    color: var(--ink-soft);
    margin-top: 2px;
    letter-spacing: 0.2px;
  }
  .signer-signature {
    font-family: "Pinyon Script", cursive;
    font-size: 17px;
    color: var(--ink);
    margin-top: 8px;
  }
  .contact {
    position: absolute;
    left: 63px;
    top: 832px;
    font-family: "Questrial", Arial, sans-serif;
    font-size: 12px;
    line-height: 14px;
    color: var(--ink-soft);
  }
  .contact-address { margin-bottom: 5px; }
  .contact-line {
    display: flex;
    align-items: center;
    gap: 6px;
    margin-top: 3px;
  }
  .contact-icon { width: 8px; height: 8px; flex: none; }
  .contact-web .domain { color: var(--brand-red); }
  .footer-band {
    position: absolute;
    left: 0;
    bottom: 0;
    width: 736px;
    height: 16px;
    background: var(--brand-red);
  }
</style>
</head>
<body>
  <main class="letterhead">
    <svg class="header-wave" viewBox="0 0 818 170" preserveAspectRatio="none" aria-hidden="true">
      <path d="M0 0 H818 V158 C700 100 520 42 380 40 C230 40 90 52 0 64 Z" fill="var(--brand-black)"/>
      <path d="M0 68 C100 56 250 45 380 45 C520 46 680 92 818 158" fill="none" stroke="var(--rule-white)" stroke-width="3"/>
      <path d="M0 74 C100 62 250 50 380 51 C520 53 680 98 810 158 C680 108 520 70 380 66 C250 64 100 82 0 106 Z" fill="var(--brand-red)"/>
    </svg>

    <header class="brand">
      <div class="brand-square"></div>
      <div class="brand-name">Maplerise<br>Trading</div>
    </header>

    <section class="letter-body">
      <p>Lorem ipsum dolor sit amet, consectetur adipiscing elit, sed do eiusmod tempor incididunt ut labore et dolore magna aliqua. Ut enim ad minim veniam, quis nostrud exercitation ullamco laboris nisi ut aliquip ex ea commodo consequat. Duis aute irure dolor in reprehenderit in voluptate velit esse cillum dolore eu fugiat nulla pariatur. Excepteur sint occaecat cupidatat non proident, sunt in culpa qui officia deserunt mollit anim id est laborum.</p>
      <p>Sed ut perspiciatis unde omnis iste natus error sit voluptatem accusantium doloremque laudantium, totam rem aperiam, eaque ipsa quae ab illo inventore veritatis et quasi architecto beatae vitae dicta sunt explicabo. Nemo enim ipsam voluptatem quia voluptas sit aspernatur aut odit aut fugit, sed quia consequuntur magni dolores eos qui ratione voluptatem sequi nesciunt. Neque porro quisquam est, qui dolorem ipsum quia dolor sit amet, consectetur, adipisci velit, sed quia non numquam eius modi tempora incidunt ut labore et dolore magnam aliquam quaerat voluptatem.</p>
      <p>But I must explain to you how all this mistaken idea of denouncing pleasure and praising pain was born and I will give you a complete account of the system, and expound the actual teachings of the great explorer of the truth, the master-builder of human happiness. No one rejects, dislikes, or avoids pleasure itself, because it is pleasure, but because those who do not know how to pursue pleasure rationally encounter consequences that are extremely painful. Nor again is there anyone who loves or pursues or desires to obtain pain of itself, because it is pain, but because occasionally circumstances occur in which toil and pain can procure him some great pleasure. To take a trivial example, which of us ever undertakes laborious physical exercise, except to obtain some advantage from it? But who has any right to find fault with a man who chooses to enjoy a pleasure that has no annoying consequences, or one who avoids a pain that produces no resultant pleasure?</p>
    </section>

    <section class="signer">
      <div class="signer-name">DANIEL MERCER</div>
      <div class="signer-role">CEO / FOUNDER</div>
      <div class="signer-signature">Signature</div>
    </section>

    <footer class="contact">
      <div class="contact-address">14 Rue Lumière,<br>Kinshasa, DRC</div>
      <div class="contact-line">
        <svg class="contact-icon" viewBox="0 0 10 10" aria-hidden="true"><path d="M2 1 L4 1 L4.6 3 L3.4 4 C4 5.4 4.6 6 6 6.6 L7 5.4 L9 6 L9 8 C9 8.6 8.6 9 8 9 C4.2 9 1 5.8 1 2 C1 1.4 1.4 1 2 1 Z" fill="var(--brand-red)"/></svg>
        <span>+243 810 555 417</span>
      </div>
      <div class="contact-line">
        <svg class="contact-icon" viewBox="0 0 10 10" aria-hidden="true"><rect x="0.5" y="2" width="9" height="6.5" fill="var(--brand-red)"/><path d="M0.8 2.3 L5 5.6 L9.2 2.3" fill="none" stroke="var(--paper)" stroke-width="0.9"/></svg>
        <span>maplerisetrade@mail.com</span>
      </div>
      <div class="contact-line contact-web">
        <svg class="contact-icon" viewBox="0 0 10 10" aria-hidden="true"><circle cx="5" cy="5" r="4.5" fill="var(--brand-red)"/><path d="M0.8 5 H9.2 M5 0.6 C3 3 3 7 5 9.4 M5 0.6 C7 3 7 7 5 9.4" fill="none" stroke="var(--paper)" stroke-width="0.7"/></svg>
        <span>www.<span class="domain">maplerisetrade</span>.com</span>
      </div>
    </footer>

    <div class="footer-band"></div>
  </main>
</body>
</html>
```